MS Word and MS Powerpoint template creation using existing logo as style guide

Create a professional looking MS Word document template and MS powerpoint template for Corvant Advisory Pty Ltd using a logo that's already been created as the style guide. Corvant is a professional services business providing strategy, governance and execution support to small and medium business, Boards and executive teams. refer design brief.

Target Market(s)

Small to medium business, Chairs, Boards, executive teams, general managers

Industry/Entity Type

Professional business services, consultancy, business support outsourcing

Other font styles liked:
• calibri

Requirements
Must have
• leverage the existing logo for colour scheme. Use the CORVANT logo type font. Fully editable templates Word and MS Powerpoint,
Nice to have
• Refer to the design brief
Should not have
• animations, cartoons, stock images of people.

```html
<!DOCTYPE html>
<html lang="en">
<head>
<meta charset="utf-8">
<title>Corvant Advisory – Presentation Template</title>
<link rel="stylesheet" href="https://fonts.googleapis.com/css2?family=Poppins:wght@300;400;500;700&display=swap">
<style>
  :root {
    --board: #4d4d4d;
    --paper: #ffffff;
    --navy: #1b2e48;
    --navy-mid: #2f4661;
    --slate: #5a697c;
    --ink: #1b2438;
    --corner-tint: #eef1f5;
  }
  * { box-sizing: border-box; margin: 0; padding: 0; }
  html, body { width: 1200px; height: 1001px; overflow: hidden; }
  body {
    background: var(--board);
    font-family: "Poppins", Arial, sans-serif;
    color: var(--ink);
    position: relative;
  }
  .slide {
    position: absolute;
    width: 455px;
    height: 256px;
    background: var(--paper);
    overflow: hidden;
    box-shadow: 0 10px 14px -8px rgba(0,0,0,.45);
  }
  .slide--cover { left: 129px; top: 78px; }
  .slide--content-a { left: 616px; top: 78px; }
  .slide--panels { left: 129px; top: 368px; }
  .slide--content-b { left: 616px; top: 368px; }
  .slide--closing { left: 129px; top: 659px; background: var(--navy); }

  .tile { position: absolute; }
  .tile--photo-grey { background: linear-gradient(135deg, #bdbdbd, #8f8f8f); }
  .tile--photo-navy { background: linear-gradient(160deg, #1f3350, #101d30); }
  .tile--photo-desk { background: linear-gradient(135deg, #d9d9d9, #9a9a9a); }

  .brand-block {
    position: absolute;
    background: var(--navy);
    color: #fff;
    display: flex; flex-direction: column; align-items: center; justify-content: center;
    text-align: center;
  }
  .brand-block__name { font-weight: 300; font-size: 23px; letter-spacing: 4px; }
  .brand-block__tagline { font-size: 7px; letter-spacing: 1px; line-height: 1.35; margin-top: 6px; }

  .badge {
    position: absolute;
    width: 68px; height: 25px;
    background: var(--navy);
    color: #fff;
    font-weight: 400; font-size: 9.5px; letter-spacing: 1.6px;
    padding-left: 1.6px;
    display: flex; align-items: center; justify-content: center;
  }

  .corner-tint { position: absolute; }
  .corner-tint--top {
    right: 0; top: 0; width: 130px; height: 90px;
    background: radial-gradient(ellipse at 100% 0%, var(--corner-tint) 0%, rgba(238,241,245,0) 70%);
  }
  .corner-tint--bottom {
    left: 0; bottom: 0; width: 130px; height: 90px;
    background: radial-gradient(ellipse at 0% 100%, var(--corner-tint) 0%, rgba(238,241,245,0) 70%);
  }

  .heading {
    position: absolute;
    font-weight: 700;
    text-transform: uppercase;
    line-height: 1.25;
    color: var(--ink);
  }
  .lead { position: absolute; font-size: 11.5px; }
  .bullets { position: absolute; list-style: none; }
  .bullets li { position: relative; padding-left: 9px; }
  .bullets li::before {
    content: ""; position: absolute; left: 0; top: .55em;
    width: 3px; height: 3px; background: currentColor;
  }

  .slide--content-a .heading { left: 55px; top: 60px; font-size: 10px; }
  .slide--content-a .lead { left: 55px; top: 99px; }
  .slide--content-a .bullets { left: 55px; top: 131px; font-size: 10px; line-height: 16.8px; }

  .partner-mark {
    position: absolute; left: 49px; top: 51px;
    display: flex; align-items: center; gap: 3px;
    font-size: 7.5px; color: var(--navy); letter-spacing: .3px;
  }
  .partner-mark__dot { width: 11px; height: 11px; border-radius: 50%; border: 1px solid var(--navy); }
  .panel { position: absolute; color: #fff; }
  .panel--tag {
    left: 46px; top: 77px; width: 87px; height: 88px; background: var(--navy);
    font-weight: 300; font-size: 9px; line-height: 1.1; padding: 25px 0 0 20px;
  }
  .panel--title {
    left: 133px; top: 51px; width: 91px; height: 140px; background: var(--navy-mid);
    font-size: 9.5px; text-align: center; line-height: 1.3;
    display: flex; align-items: center; justify-content: center;
  }
  .panel--list { left: 224px; top: 51px; width: 180px; height: 140px; background: var(--slate); }
  .panel--list .bullets { left: 9px; top: 40px; font-size: 5.6px; line-height: 1.3; }
  .panel--list .bullets li { margin-bottom: 7px; }
  .rule { position: absolute; left: 26px; top: 229px; width: 341px; height: 1px; background: var(--navy); }
  .rule--accent { width: 65px; height: 2.5px; top: 228px; }

  .tag-box {
    position: absolute; left: 50px; top: 69px; width: 73px; height: 60px;
    background: var(--navy); color: #fff;
    font-weight: 300; font-size: 8.5px; line-height: 1.15; padding: 8px 0 0 11px;
  }
  .slide--content-b .heading { left: 151px; top: 69px; font-size: 9.5px; }
  .slide--content-b .bullets { left: 151px; top: 106px; font-size: 5.6px; line-height: 11.6px; }

  .closing-bg {
    position: absolute; inset: 0;
    background: radial-gradient(ellipse at 75% 30%, #3b5270 0%, transparent 55%),
                linear-gradient(180deg, #223653, #1b2e48);
  }
  .closing-title {
    position: absolute; left: 0; right: 0; top: 104px;
    text-align: center; color: #fff; font-weight: 700; font-size: 29px;
  }
</style>
</head>
<body>

<section class="slide slide--cover">
  <div class="tile tile--photo-grey" style="left:28px;top:28px;width:115px;height:94px" role="img" aria-label="Greyscale stock market chart photo"></div>
  <div class="tile tile--photo-navy" style="left:150px;top:28px;width:115px;height:94px" role="img" aria-label="Navy-tinted office tower photo"></div>
  <div class="tile tile--photo-desk" style="left:271px;top:28px;width:155px;height:94px" role="img" aria-label="Greyscale photo of reports on a desk"></div>
  <div class="tile tile--photo-navy" style="left:28px;top:132px;width:115px;height:95px" role="img" aria-label="Dark office building photo"></div>
  <div class="tile tile--photo-grey" style="left:150px;top:132px;width:115px;height:95px" role="img" aria-label="Greyscale photo of stacked coins"></div>
  <div class="brand-block" style="left:271px;top:132px;width:155px;height:95px">
    <div class="brand-block__name">CORVANT</div>
    <div class="brand-block__tagline">CONNECTING STRATEGY,<br>GOVERNANCE &amp; EXECUTION</div>
  </div>
</section>

<section class="slide slide--content-a">
  <div class="corner-tint corner-tint--top" role="img" aria-label="Decorative corner line ornament"></div>
  <div class="corner-tint corner-tint--bottom" role="img" aria-label="Decorative corner line ornament"></div>
  <h2 class="heading">Consectetuer adipiscing elit, sed diam nonummy<br>nibh euismod tincidunt ut laoreet</h2>
  <p class="lead">Dolore magna aliquam erat volutpat.</p>
  <ul class="bullets">
    <li>Vel illum dolore eu feugiat nulla facilisis.</li>
    <li>Ut wisi enim ad minim veniam, quis nostrud</li>
    <li>Quis nostrud exerci tation ullamcorper suscipit lobortis nisl ut aliquip</li>
  </ul>
  <div class="badge" style="left:363px;top:218px">CORVANT</div>
</section>

<section class="slide slide--panels">
  <div class="partner-mark"><span class="partner-mark__dot"></span>HARBOR RIDGE</div>
  <div class="panel panel--tag">Connecting<br>Strategy<br>Governance<br>&amp; Execution</div>
  <div class="panel panel--title">WISI ENIM<br>MINIM VENIAM<br>NOSTRUD</div>
  <div class="panel panel--list">
    <ul class="bullets">
      <li>Vel illum dolore eu feugiat nulla facilisis.</li>
      <li>Quis nostrud exerci tation ullamcorper<br>suscipit lobortis nisl ut aliquip</li>
      <li>Ut wisi enim ad minim veniam, quis nostrud</li>
      <li>Exerci tation ullamcorper suscipit lobortis</li>
    </ul>
  </div>
  <div class="rule"></div>
  <div class="rule rule--accent"></div>
  <div class="badge" style="left:365px;top:217px">CORVANT</div>
</section>

<section class="slide slide--content-b">
  <div class="corner-tint corner-tint--top" role="img" aria-label="Decorative corner line ornament"></div>
  <div class="corner-tint corner-tint--bottom" role="img" aria-label="Decorative corner line ornament"></div>
  <div class="tag-box">Connecting<br>Strategy<br>Governance<br>&amp; Execution</div>
  <h2 class="heading">Adipiscing elit, sed diam nonummy<br>nibh euismod tincidunt</h2>
  <ul class="bullets">
    <li>Vel illum dolore eu feugiat nulla facilisis.</li>
    <li>Ut wisi enim ad minim veniam, quis nostrud</li>
    <li>Quis nostrud exerci tation ullamcorper suscipit lobortis nisl ut aliquip</li>
    <li>Dolore eu feugiat nulla facilisis.</li>
    <li>Exerci tation ullamcorper suscipit lobortis nisl ut aliquip</li>
  </ul>
  <div class="badge" style="left:363px;top:218px">CORVANT</div>
</section>

<section class="slide slide--closing">
  <div class="closing-bg" role="img" aria-label="Navy-tinted financial growth chart background"></div>
  <h2 class="closing-title">Thank you</h2>
</section>

</body>
</html>
```